Need a business card for our overland brand!

We had the logo made and we need a great design for our business card. Use the logo provide or tweak it however you see fit.

Contact Information for Business Card

Name, Title, Telephone, email, website

```html
<!DOCTYPE html>
<html lang="en">
<head>
<meta charset="utf-8">
<title>Summit Trail – Business Card</title>
<link href="https://fonts.googleapis.com/css2?family=Montserrat:wght@400;500;700&family=Lato:wght@400&display=swap" rel="stylesheet">
<style>
  :root {
    --navy: #253a52;
    --cyan: #1fa0c1;
    --white: #ffffff;
    --stage: #d3d4d6;
    --grey-text: #555b63;
  }
  * { margin: 0; padding: 0; box-sizing: border-box; }
  html, body {
    width: 900px; height: 1200px; overflow: hidden;
    background: var(--stage);
  }
  .card {
    position: absolute; left: 130px;
    width: 640px; height: 367px;
    overflow: hidden;
  }
  .card svg.decor { position: absolute; inset: 0; }
  .card--front { top: 210px; background: var(--navy); }
  .card--back { top: 626px; background: var(--white); }

  .wordmark {
    position: absolute;
    font-family: 'Montserrat', sans-serif;
    font-weight: 700;
    text-transform: uppercase;
    line-height: 1;
    text-align: center;
  }
  .card--front .wordmark {
    left: 0; right: 0; top: 122px;
    color: var(--white);
    font-size: 74px; letter-spacing: -1px;
  }
  .card--front .wordmark span { display: block; margin-bottom: 12px; }
  .card--back .wordmark {
    left: 58px; width: 220px; top: 120px;
    color: var(--navy);
    font-size: 48px; letter-spacing: -1px;
  }
  .card--back .wordmark span { display: block; margin-bottom: 8px; }

  .divider {
    position: absolute; left: 298px; top: 55px;
    width: 2px; height: 204px; background: var(--cyan);
  }
  .person { position: absolute; left: 334px; top: 64px; font-family: 'Montserrat', sans-serif; }
  .person__name { font-size: 22px; font-weight: 700; color: var(--navy); letter-spacing: 1px; }
  .person__title { margin-top: 8px; font-size: 15px; font-weight: 500; color: #222; letter-spacing: 0.5px; }

  .contacts { position: absolute; left: 334px; top: 144px; list-style: none; }
  .contacts li {
    display: flex; align-items: center; height: 20px; margin-bottom: 11px;
    font-family: 'Lato', sans-serif; font-size: 12.5px; color: var(--grey-text); letter-spacing: 0.3px;
  }
  .contacts svg { width: 22px; height: 18px; margin-right: 9px; fill: var(--cyan); flex: none; }
</style>
</head>
<body>

<section class="card card--front">
  <svg class="decor" viewBox="0 0 640 367" width="640" height="367">
    <path d="M0 0 H128 C60 40 10 160 0 300 Z" fill="var(--cyan)"/>
    <path d="M640 68 C625 200 590 300 510 367 H640 Z" fill="var(--cyan)"/>
    <path d="M94 40 C45 100 12 190 4 300" fill="none" stroke="var(--cyan)" stroke-width="4" stroke-linecap="round"/>
    <path d="M638 75 C620 180 590 260 544 326" fill="none" stroke="var(--cyan)" stroke-width="4" stroke-linecap="round"/>
  </svg>
  <div class="wordmark"><span>Summit</span><span>Trail</span></div>
</section>

<section class="card card--back">
  <svg class="decor" viewBox="0 0 641 367" width="640" height="367">
    <path d="M641 154 C560 290 360 360 118 367 H641 Z" fill="var(--cyan)"/>
    <path d="M573 211 C480 300 320 350 141 364" fill="none" stroke="var(--cyan)" stroke-width="6" stroke-linecap="round"/>
  </svg>
  <div class="wordmark"><span>Summit</span><span>Trail</span></div>
  <div class="divider"></div>
  <div class="person">
    <div class="person__name">DANIEL HARPER</div>
    <div class="person__title">MANAGING DIRECTOR</div>
  </div>
  <ul class="contacts">
    <li><svg viewBox="0 0 22 18"><path d="M11 0a6 6 0 0 0-6 6c0 4.5 6 12 6 12s6-7.5 6-12a6 6 0 0 0-6-6zm0 8.5A2.5 2.5 0 1 1 11 3.5a2.5 2.5 0 0 1 0 5z"/></svg>STREET, CITY, COUNTRY</li>
    <li><svg viewBox="0 0 22 18"><path d="M0 2h22v14H0z"/><path d="M1 3l10 7 10-7" fill="none" stroke="#fff" stroke-width="1.6"/></svg>LOREMIPSUM@MAIL.COM</li>
    <li><svg viewBox="0 0 22 18"><circle cx="11" cy="9" r="8.5"/><path d="M6 5c2 0 3 1 3 3s-2 2-2 4M14 3c-1 2 1 3 2 3s2 2 1 4" fill="none" stroke="#fff" stroke-width="1.4"/></svg>WWW.LOREM IPSUM.COM</li>
    <li><svg viewBox="0 0 22 18"><path d="M6 1l3 3-2 2.5c1 2 3 4 5 5L14.5 9l3 3-2 3c-6 0-11-5-12-11z"/></svg>01 8000 00 00</li>
  </ul>
</section>

</body>
</html>
```